Customizable Gift Note Card Design

I need a gift note card designed for my Healthy Snacks Care Package company. I need to be able to customize each card with the customer's gift message to the recipient and print to a standard printer.

The card should be single-sided 5 x 7, include our logo, keep colors and graphics simple since they will be printed for each individual order on a standard printer. I would like the following quote to be included in a small and subtle way: "Food is symbolic of love when words are inadequate." —Bertram K. Osslund. Our website thebrightpantrybites.example should also be included.

I have included pictures of our product packaging for reference.

Target Market(s)

Gift recipients: Students, people recovering from illness, housewarming, thank you gifts...etc.

Industry/Entity Type

It Company

Colors

Designer to choose colors to be used in the design.

Requirements
Must have
• We are looking for a simple, cute and elegant gift card that reflects our branding. Must be customizable and printable on a standard printer.
• Must be single-sided 5x7.

```html
<!DOCTYPE html>
<html lang="en">
<head>
<meta charset="utf-8">
<title>The Bright Pantry – Gift Note Card</title>
<link href="https://fonts.googleapis.com/css2?family=Lobster&family=Inconsolata:wght@400&display=swap" rel="stylesheet">
<style>
  :root {
    --canvas-bg: #e7e8ea;
    --kraft: #b9a47b;
    --kraft-light: #c3ae85;
    --kraft-dark: #ab9469;
    --ink: #0d0b09;
    --ink-soft: #2a2418;
    --accent-red: #8e1c1c;
    --rule: #1b1a17;
  }
  * { margin: 0; padding: 0; box-sizing: border-box; }
  html, body {
    width: 1200px;
    height: 1186px;
    overflow: hidden;
    background: var(--canvas-bg);
  }
  .note-card {
    position: absolute;
    left: 282px;
    top: 148px;
    width: 637px;
    height: 890px;
    background:
      radial-gradient(ellipse at 30% 25%, var(--kraft-light) 0%, transparent 55%),
      radial-gradient(ellipse at 75% 80%, var(--kraft-light) 0%, transparent 50%),
      linear-gradient(180deg, var(--kraft) 0%, var(--kraft-dark) 100%);
  }
  .brand-mark {
    position: absolute;
    left: 258px;
    top: 110px;
    width: 120px;
    height: 120px;
    border-radius: 50%;
    background: var(--ink);
  }
  .brand-name {
    position: absolute;
    left: 0;
    width: 100%;
    top: 392px;
    text-align: center;
    font-family: "Lobster", cursive;
    font-size: 62px;
    line-height: 1;
    color: var(--ink);
  }
  .divider {
    position: absolute;
    left: 65px;
    width: 497px;
    height: 1px;
    background: linear-gradient(90deg, transparent 0%, var(--rule) 12%, var(--rule) 88%, transparent 100%);
  }
  .divider--top { top: 524px; }
  .divider--bottom { top: 786px; }
  .quote {
    position: absolute;
    left: 0;
    width: 100%;
    top: 560px;
    text-align: center;
    font-family: "Lobster", cursive;
    font-size: 39px;
    line-height: 68px;
    color: var(--ink);
  }
  .quote-author {
    position: absolute;
    right: 124px;
    top: 697px;
    font-family: "Lobster", cursive;
    font-size: 26px;
    color: var(--ink-soft);
  }
  .website {
    position: absolute;
    left: 0;
    width: 100%;
    top: 817px;
    padding-left: 26px;
    text-align: center;
    font-family: "Inconsolata", monospace;
    font-size: 21px;
    letter-spacing: 0.5px;
    color: var(--accent-red);
  }
</style>
</head>
<body>
  <main class="note-card">
    <div class="brand-mark" aria-hidden="true"></div>
    <h1 class="brand-name">The Bright Pantry</h1>
    <div class="divider divider--top"></div>
    <blockquote class="quote">
      Food is symbolic of love when<br>words are inadequate.
    </blockquote>
    <p class="quote-author">Bertram K. Osslund</p>
    <div class="divider divider--bottom"></div>
    <p class="website">www.thebrightpantrybites.example</p>
  </main>
</body>
</html>
```